Business Card Design

We need a business card design that can also be aplied for postcards. We are a small indie record company that also do consulting, and development of independat artitst . I already have the name and the basic idea of what i am looking for but i am open to any suggestion.
Info for the card
Name of the company : Velmora Records
NAME : Tomas Invaldi
PHONE : 208-5536142
EMAIL : hello@velmorarecords.example
WEB: www.velmorarecords.example
Target Market(s)
Male - Female independent musicians ages 18 to 45
Industry/Entity Type
Record Company
Contact Information for Business Card
Independant records company that also works in consulting for music business models for independent artists
Look and feel
Each slider illustrates characteristics of the customer's brand and the style your logo design should communicate.

```html
<!DOCTYPE html>
<html lang="en">
<head>
<meta charset="utf-8">
<title>Velmora Records — Business Card</title>
<link rel="stylesheet" href="https://fonts.googleapis.com/css2?family=PT+Sans:wght@400;700&family=PT+Sans+Narrow:wght@700&display=swap">
<style>
  :root {
    --page-bg: #ffffff;
    --frame-line: #c8c8c8;
    --front-deep: #1f1a3a;
    --front-violet: #4a2c6e;
    --front-teal: #1e5a6a;
    --front-magenta: #b0307a;
    --back-light: #f1f1f3;
    --back-mist: #e6e6ea;
    --logo-light: #ffffff;
    --logo-dark: #1c1c1c;
    --muted-text: #6a6a6a;
    --name-text: #111111;
    --contact-blue: #1f7fc2;
  }
  * { box-sizing: border-box; margin: 0; padding: 0; }
  html, body {
    width: 1200px;
    height: 998px;
    overflow: hidden;
    background: var(--page-bg);
  }
  .sheet {
    position: relative;
    width: 1200px;
    height: 998px;
    border: 2px solid var(--frame-line);
    background: var(--page-bg);
    font-family: "PT Sans", sans-serif;
  }
  .card {
    position: absolute;
    width: 596px;
    height: 336px;
    overflow: hidden;
  }
  .card--front { left: 102px; top: 134px; }
  .card--back { left: 496px; top: 494px; }

  .card__art {
    position: absolute;
    inset: 0;
  }
  .card--front .card__art {
    background:
      radial-gradient(ellipse 60% 70% at 75% 45%, rgba(255,255,255,0.45), transparent 60%),
      radial-gradient(ellipse 50% 60% at 30% 80%, var(--front-magenta), transparent 70%),
      radial-gradient(ellipse 60% 60% at 85% 20%, var(--front-teal), transparent 70%),
      linear-gradient(135deg, var(--front-deep), var(--front-violet) 55%, var(--front-deep));
  }
  .card--back .card__art {
    background:
      radial-gradient(ellipse 50% 60% at 30% 65%, rgba(255,255,255,0.9), transparent 70%),
      radial-gradient(ellipse 50% 50% at 85% 15%, #f7eef6, transparent 70%),
      linear-gradient(135deg, var(--back-light), var(--back-mist));
  }

  .wordmark {
    position: absolute;
    font-family: "PT Sans", sans-serif;
    font-weight: 400;
    line-height: 1;
    text-align: right;
  }
  .wordmark__name { display: block; }
  .wordmark__sub { display: block; letter-spacing: 1px; }

  .card--front .wordmark {
    left: 52px;
    top: 112px;
    width: 272px;
    color: var(--logo-light);
  }
  .card--front .wordmark__name { font-size: 68px; }
  .card--front .wordmark__sub { font-size: 24px; margin-top: 2px; }

  .card--back .wordmark {
    left: 208px;
    top: 44px;
    width: 192px;
    color: var(--logo-dark);
  }
  .card--back .wordmark__name { font-size: 46px; }
  .card--back .wordmark__sub { font-size: 16px; margin-top: 0; }

  .contact {
    position: absolute;
    left: 0;
    width: 100%;
    text-align: center;
  }
  .contact__web {
    position: absolute;
    left: 180px;
    top: 118px;
    width: 260px;
    text-align: center;
    font-size: 16px;
    color: var(--muted-text);
  }
  .contact__block {
    position: absolute;
    left: 150px;
    top: 224px;
    width: 340px;
    text-align: center;
  }
  .contact__name {
    font-family: "PT Sans Narrow", sans-serif;
    font-weight: 700;
    font-size: 24px;
    color: var(--name-text);
    margin-bottom: 8px;
  }
  .contact__line {
    font-size: 16px;
    color: var(--contact-blue);
    line-height: 30px;
  }
</style>
</head>
<body>
  <main class="sheet">
    <section class="card card--front">
      <div class="card__art" role="img" aria-label="Colourful light-streak artwork with music notes and a dancing guitarist silhouette"></div>
      <div class="wordmark">
        <span class="wordmark__name">Velmora</span>
        <span class="wordmark__sub">RECORDS</span>
      </div>
    </section>

    <section class="card card--back">
      <div class="card__art" role="img" aria-label="Faded light-streak artwork with a pale guitarist silhouette"></div>
      <div class="wordmark">
        <span class="wordmark__name">Velmora</span>
        <span class="wordmark__sub">RECORDS</span>
      </div>
      <p class="contact__web">www.velmorarecords.example</p>
      <div class="contact__block">
        <p class="contact__name">Tomas Invaldi</p>
        <p class="contact__line">Call: 208-5536142</p>
        <p class="contact__line">Email: hello@velmorarecords.example</p>
      </div>
    </section>
  </main>
</body>
</html>
```